MEDICAL CLINIC LETTERHEAD

Design is a letterhead for a non-profit medical center. The name of the clinic is VYRLOTEN Community Health Center. Although the full name must be included, the community health center part is more of a description and should be less visible - i attached an example of what I mean by that (ATTACHED IMAGE IS AN EXAMPLE OF FONT SIZES NOT A DESIGN IDEA). Please design something modern, cool looking and unique because I can always download free templates.
Phone, email, website and etc will be added later.

Industry/Entity Type

MEDICAL

```html
<!DOCTYPE html>
<html lang="en">
<head>
<meta charset="utf-8">
<title>VYRLOTEN Community Health Center — Letterhead</title>
<link rel="stylesheet" href="https://fonts.googleapis.com/css2?family=Questrial&family=Roboto:wght@400&display=swap">
<style>
  :root {
    --navy: #082a57;
    --ink: #555a60;
    --paper: #f4f4f4;
    --backdrop: #e6e6e6;
    --white: #ffffff;
  }
  * { margin: 0; padding: 0; box-sizing: border-box; }
  html, body {
    width: 1023px;
    height: 1200px;
    overflow: hidden;
    background: var(--backdrop);
  }
  .letterhead {
    position: absolute;
    left: 89px;
    top: 8px;
    width: 845px;
    height: 1185px;
    background: var(--paper);
    font-family: "Questrial", sans-serif;
    color: var(--ink);
  }
  .brand {
    position: absolute;
    top: 88px;
    left: 0;
    width: 100%;
    display: flex;
    flex-direction: column;
    align-items: center;
  }
  .brand-line {
    display: flex;
    align-items: center;
    gap: 12px;
  }
  .brand-mark {
    width: 14px;
    height: 14px;
    background: var(--navy);
  }
  .brand-name {
    font-family: "Questrial", sans-serif;
    font-weight: 400;
    font-size: 36px;
    line-height: 1;
    color: var(--navy);
  }
  .brand-descriptor {
    margin-top: 8px;
    font-family: "Questrial", sans-serif;
    font-size: 14px;
    color: var(--ink);
  }
  .letter-body {
    position: absolute;
    left: 80px;
    top: 310px;
    width: 695px;
  }
  .salutation {
    font-size: 16px;
    margin-bottom: 37px;
  }
  .letter-body p.copy {
    font-size: 12.6px;
    line-height: 18px;
    text-align: justify;
    margin-bottom: 18px;
  }
  .letter-body p.copy.spaced { margin-top: 36px; }
  .closing {
    font-size: 13px;
    margin-top: 72px;
  }
  .contact-band {
    position: absolute;
    left: 55px;
    top: 1082px;
    width: 721px;
    height: 33px;
    background: var(--navy);
    color: var(--white);
    font-family: "Roboto", sans-serif;
    font-size: 13px;
    display: flex;
    align-items: center;
    justify-content: center;
    gap: 16px;
  }
  .contact-item { display: flex; align-items: center; gap: 6px; white-space: nowrap; }
  .contact-item svg { width: 11px; height: 11px; fill: var(--white); }
</style>
</head>
<body>
<main class="letterhead">
  <header class="brand">
    <div class="brand-line">
      <span class="brand-mark"></span>
      <span class="brand-name">VYRLOTEN</span>
    </div>
    <div class="brand-descriptor">Community Health Center</div>
  </header>

  <section class="letter-body">
    <p class="salutation">Dear Elias,</p>
    <p class="copy">Donec malesuada orci vitae nulla accumsan porta a id massa. Quisque accumsan iaculis magna sit amet fringilla. Maecenas consequat, magna eget tincidunt semper, odio nibh rutrum mi, id feugiat ante nisi eu risus. Vestibulum nunc orci, rhoncus a placerat in, ultricies in mi. Cras mattis varius eros, vel fringilla nisi suscipit eget. Quisque sceleris&shy;que sagittis nulla at porttitor.</p>
    <p class="copy">Lorem ipsum dolor sit amet, consectetur adipiscing elit. Donec orci purus, luctus vitae dignissim eu, iaculis sed purus. Vivamus faucibus, ipsum nec aliquet viverra, leo mauris condimentum ligula, sit amet sagittis enim ligula quis arcu. Nam egestas tortor id nisi porttitor mattis. In tortor ante, ultricies in suscipit a, tempus non massa. Vivamus et auctor mi. Fusce vel massa nulla. Phasellus nec eros mauris, et scelerisque orci.</p>
    <p class="copy spaced">It is a long established fact that a reader will be distracted by the readable content of a page when looking at its layout. The point of using Lorem Ipsum is that it has a more-or-less normal distribution of letters, as opposed to using 'Content here, content here', making it look like readable English. Many desktop publishing packagest</p>
    <p class="copy">Sed id augue vitae urna euismod commodo aliquet a quam. Pellentesque arcu velit, cursus et malesuada ut, con&shy;sequat et diam. Nullam erat sem, rhoncus id ullamcorper vitae, rhoncus et arcu. In ultricies ultricies nulla, ut rutrum nisi iaculis at. Donec eu magna a metus ornare faucibus. Fusce aliquet faucibus ultricies. Morbi semper, est id tincid&shy;unt gravida, sem arcu adipiscing lacus, ac bibendum nulla leo eu purus. Quisque nec diam sed risus consectetur a ccumsan quis quis nibh. Vestibulum id purus lorem.</p>
    <p class="closing">Sincerely,</p>
  </section>

  <footer class="contact-band">
    <span class="contact-item">PO Box 412 Harlow Falls, North Dakota 58720</span>
    <span class="contact-item">
      <svg viewBox="0 0 24 24" aria-hidden="true"><path d="M6.6 10.8a15.1 15.1 0 0 0 6.6 6.6l2.2-2.2c.3-.3.7-.4 1-.2 1.1.4 2.3.6 3.6.6.6 0 1 .4 1 1V20c0 .6-.4 1-1 1A17 17 0 0 1 3 4c0-.6.4-1 1-1h3.5c.6 0 1 .4 1 1 0 1.3.2 2.5.6 3.6.1.3 0 .7-.2 1z"/></svg>
      (555) 310.4827
    </span>
    <span class="contact-item">
      <svg viewBox="0 0 24 24" aria-hidden="true"><path d="M2 5h20v14H2z M2 5l10 8 10-8" fill="none" stroke="#fff" stroke-width="2"/><path d="M2 5h20l-10 8z"/></svg>
      info@vyrloten.org
    </span>
    <span class="contact-item">
      <svg viewBox="0 0 24 24" aria-hidden="true"><circle cx="12" cy="12" r="10"/><path d="M2 12h20M12 2c3 3 3 17 0 20M12 2c-3 3-3 17 0 20" fill="none" stroke="#082a57" stroke-width="1.6"/></svg>
      www.vyrloten.org
    </span>
  </footer>
</main>
</body>
</html>
```